Artwork flyer ( named LO MI RA ) for my music festival

I need a flyer artwork created for my indie pop, rock, hip-hop and dance music festival as soon as possible. The festival is for ages 18 to 30. Need flyer to be able to be abstracted so i can export into different social media
sizes etc

Here is some information around the music festival details.

Title: LO MI RA ( music festival)

Artists :
PELI Fold
Moira Flint
KRTs
The Brellows
Zint Vobs
Tidal Baron
Velvet no
Amber Frost

Venue: Harrowby Paddock Club
Date: Saturday 25th March
Tickets: www.gatelyne.com.au

Logo Text

LOMI RA ( or LO MI RA)

```html
<!DOCTYPE html>
<html lang="en">
<head>
<meta charset="utf-8">
<title>LOMI RA Music Festival Flyer</title>
<link rel="stylesheet" href="https://fonts.googleapis.com/css2?family=Bebas+Neue&family=Montserrat:wght@400;500;800;900&family=Roboto:wght@700&display=swap">
<style>
  :root{
    --page:#ffffff;
    --ink:#030405;
    --white:#ffffff;
    --cyan:#00f0f0;
    --yellow:#ffef00;
    --magenta:#ff1ee8;
    --red:#ff1147;
    --edge:#9a9a9a;
  }
  *{margin:0;padding:0;box-sizing:border-box}
  html,body{width:1200px;height:1200px;overflow:hidden;background:var(--page)}
  .flyer{position:absolute;left:303px;top:227px;width:601px;height:752px;background:var(--ink);border:1px solid var(--edge);overflow:hidden;color:var(--white)}
  .hero-art{position:absolute;left:0;top:0;width:100%;height:175px;
    background:radial-gradient(ellipse 45% 55% at 50% 35%, rgba(255,40,70,.75), rgba(120,20,60,.4) 55%, transparent 80%),
    linear-gradient(180deg,#1a2550 0%,#221a45 45%,#0b0d18 85%,var(--ink) 100%)}
  .floor-art{position:absolute;left:0;bottom:0;width:100%;height:175px;
    background:radial-gradient(ellipse 40% 60% at 72% 30%, rgba(40,170,110,.35), transparent 70%),
    radial-gradient(ellipse 50% 60% at 30% 90%, rgba(200,40,80,.3), transparent 70%),
    linear-gradient(180deg,var(--ink) 0%,#0e1a20 40%,#1a1222 100%)}
  .row{position:absolute;left:0;width:100%;text-align:center;white-space:nowrap}
  .festival-name{top:80px;font-family:'Montserrat',sans-serif;font-weight:900;font-size:88px;line-height:88px;letter-spacing:2px;color:var(--cyan)}
  .festival-tag{top:176px;font-family:'Montserrat',sans-serif;font-weight:900;font-size:35px;line-height:38px;letter-spacing:-1px;color:var(--red)}
  .chevrons{position:absolute}
  .dots{position:absolute;top:243px}
  .lineup-intro{top:259px;font-family:'Montserrat',sans-serif;font-weight:400;font-size:16px;line-height:24px;letter-spacing:.2px}
  .artists{font-family:'Bebas Neue',sans-serif;font-size:34px;line-height:34px;letter-spacing:.6px}
  .artists .sep{display:inline-block;width:7px;height:7px;border-radius:50%;background:var(--cyan);margin:0 20px;vertical-align:middle;position:relative;top:-3px}
  .artists-1{top:324px}
  .artists-2{top:388px}
  .artists-3{top:452px}
  .marker{position:absolute;top:402px}
  .divider{position:absolute;left:32px;width:537px;top:511px;height:3px;background:var(--red)}
  .venue-label{top:529px;font-family:'Montserrat',sans-serif;font-weight:500;font-size:14px;line-height:18px}
  .venue-name{top:548px;font-family:'Montserrat',sans-serif;font-weight:800;font-size:26px;line-height:32px}
  .date-band{position:absolute;left:111px;top:588px;width:380px;height:42px;background:var(--cyan);color:var(--ink);text-align:center;font-family:'Montserrat',sans-serif;font-weight:800;font-size:29px;line-height:42px}
  .tickets-label{top:648px;font-family:'Roboto',sans-serif;font-weight:700;font-size:19px;line-height:24px}
  .tickets-url{top:672px;font-family:'Roboto',sans-serif;font-weight:700;font-size:30px;line-height:36px}
  .age-badge{position:absolute;left:523px;top:694px;width:50px;height:50px;border:3px solid var(--yellow);border-radius:50%;text-align:center;font-family:'Bebas Neue',sans-serif;font-size:27px;line-height:46px}
</style>
</head>
<body>
<main class="flyer">
  <div class="hero-art" role="img" aria-label="Neon-lit red and blue futuristic tunnel photograph"></div>
  <div class="floor-art" role="img" aria-label="Glowing multicoloured wireframe grid floor"></div>

  <h1 class="row festival-name">LOMIRA</h1>

  <svg class="chevrons" style="left:64px;top:184px" width="60" height="28" viewBox="0 0 60 28" aria-hidden="true">
    <g fill="none" stroke="var(--yellow)" stroke-width="3"><path d="M2 2l14 12-14 12"/><path d="M14 2l14 12-14 12"/><path d="M26 2l14 12-14 12"/><path d="M38 2l14 12-14 12"/></g>
  </svg>
  <p class="row festival-tag">MUSIC FESTIVAL</p>
  <svg class="chevrons" style="left:481px;top:184px" width="60" height="28" viewBox="0 0 60 28" aria-hidden="true">
    <g fill="none" stroke="var(--yellow)" stroke-width="3"><path d="M58 2L44 14l14 12"/><path d="M46 2L32 14l14 12"/><path d="M34 2L20 14l14 12"/><path d="M22 2L8 14l14 12"/></g>
  </svg>

  <svg class="dots" style="left:17px" width="44" height="55" viewBox="0 0 44 55" aria-hidden="true">
    <defs><pattern id="dotgrid" width="11.5" height="11.5" patternUnits="userSpaceOnUse"><circle cx="4.5" cy="4.5" r="4.3" fill="var(--cyan)"/></pattern></defs>
    <rect width="44" height="55" fill="url(#dotgrid)"/>
  </svg>
  <svg class="dots" style="left:534px" width="44" height="55" viewBox="0 0 44 55" aria-hidden="true">
    <rect width="44" height="55" fill="url(#dotgrid)"/>
  </svg>

  <p class="row lineup-intro">LINE UP FEATURING<br>IN ALPHABETICAL ORDER</p>

  <p class="row artists artists-1">Amber Frost<span class="sep"></span>KRTs<span class="sep"></span>PELI Fold</p>
  <p class="row artists artists-2">Tidal Baron<span class="sep"></span>Zint Vobs</p>
  <p class="row artists artists-3">Moira Flint<span class="sep"></span>Velvet No<span class="sep"></span>The Brellows</p>

  <svg class="marker" style="left:15px" width="21" height="40" viewBox="0 0 21 40" aria-hidden="true"><path d="M0 0L21 20 0 40z" fill="var(--red)"/></svg>
  <svg class="marker" style="left:564px" width="21" height="40" viewBox="0 0 21 40" aria-hidden="true"><path d="M21 0L0 20l21 20z" fill="var(--red)"/></svg>

  <div class="divider"></div>

  <p class="row venue-label">Venue :</p>
  <svg class="chevrons" style="left:103px;top:556px" width="32" height="16" viewBox="0 0 32 16" aria-hidden="true">
    <g fill="none" stroke="var(--yellow)" stroke-width="2"><path d="M1 1l8 7-8 7"/><path d="M8 1l8 7-8 7"/><path d="M15 1l8 7-8 7"/><path d="M22 1l8 7-8 7"/></g>
  </svg>
  <p class="row venue-name">Harrowby Paddock Club</p>
  <svg class="chevrons" style="left:466px;top:556px" width="32" height="16" viewBox="0 0 32 16" aria-hidden="true">
    <g fill="none" stroke="var(--yellow)" stroke-width="2"><path d="M31 1l-8 7 8 7"/><path d="M24 1l-8 7 8 7"/><path d="M17 1L9 8l8 7"/><path d="M10 1L2 8l8 7"/></g>
  </svg>

  <p class="date-band">Saturday 25th March</p>

  <p class="row tickets-label">Tickets :</p>
  <p class="row tickets-url">www.gatelyne.com.au</p>

  <div class="age-badge">18+</div>
</main>
</body>
</html>
```